Tarvel Ridge LLC

Need Professional Business cards for New Investment Fund

Target Market(s)

High Quality investors

Industry/Entity Type

Financial

Contact Information for Business Card

Phone Number +1 555 284 6193
Name Pavel Orlinsky
Title Fund Manager
email po@FundTarvel.example
Website www.FundTarvel.example

Colors

Designer to choose colors to be used in the design.

Requirements
Must have
• Must have our Logo and all of the above. Must be made so lettering and loge can be raised

```html
<!DOCTYPE html>
<html lang="en">
<head>
<meta charset="utf-8">
<title>Tarvel Ridge LLC – Business Cards</title>
<link href="https://fonts.googleapis.com/css2?family=Mulish:wght@400;700;800&display=swap" rel="stylesheet">
<style>
  :root {
    --backdrop: #edecea;
    --forest: #434f42;
    --leaf: #5cb947;
    --paper: #ffffff;
  }
  * { margin: 0; padding: 0; box-sizing: border-box; }
  html, body {
    width: 1200px; height: 900px; overflow: hidden;
    background: var(--backdrop);
    font-family: "Mulish", Arial, sans-serif;
  }
  .sheet { position: relative; width: 1200px; height: 900px; }
  .card {
    position: absolute; top: 309px;
    width: 475px; height: 282px;
    display: flex; overflow: hidden;
  }
  .card--front { left: 97px; }
  .card--back { left: 628px; }

  .panel { height: 100%; position: relative; }
  .panel--forest { background: var(--forest); }
  .panel--leaf { background: var(--leaf); }

  .card--front .panel { width: 50%; }
  .front-name {
    position: absolute; left: 0; right: 0; top: 50%;
    transform: translateY(-50%);
    text-align: center;
    color: var(--paper);
    font-weight: 800; font-size: 22px; letter-spacing: 2px;
  }

  .card--back .panel--leaf { width: 219px; display: flex; align-items: center; justify-content: center; }
  .card--back .panel--forest { flex: 1; }
  .back-name {
    color: var(--paper);
    font-weight: 800; font-size: 17px; letter-spacing: 1.5px;
  }

  .identity {
    position: absolute; left: 23px; top: 90px;
    padding-left: 19px;
    color: var(--paper);
  }
  .identity::before {
    content: ""; position: absolute; left: 0; top: 0;
    width: 11px; height: 37px; background: var(--leaf);
  }
  .identity__name { font-weight: 700; font-size: 17.5px; line-height: 19px; letter-spacing: 0.3px; }
  .identity__title { font-weight: 400; font-size: 14px; line-height: 20px; margin-top: 3px; }

  .contacts {
    position: absolute; left: 22px; top: 140px;
    list-style: none; color: var(--paper);
    font-size: 12.5px;
  }
  .contacts li { display: flex; align-items: center; height: 19px; }
  .contacts svg { width: 12px; height: 12px; margin-right: 8px; fill: var(--paper); flex: none; }
</style>
</head>
<body>
<div class="sheet">
  <section class="card card--front">
    <div class="panel panel--forest"></div>
    <div class="panel panel--leaf"></div>
    <div class="front-name">TARVEL RIDGE</div>
  </section>

  <section class="card card--back">
    <div class="panel panel--leaf">
      <div class="back-name">TARVEL RIDGE</div>
    </div>
    <div class="panel panel--forest">
      <div class="identity">
        <div class="identity__name">PAVEL ORLINSKY</div>
        <div class="identity__title">Fund Manager</div>
      </div>
      <ul class="contacts">
        <li>
          <svg viewBox="0 0 24 24" aria-hidden="true"><path d="M6.6 10.8c1.4 2.8 3.8 5.1 6.6 6.6l2.2-2.2c.3-.3.7-.4 1-.2 1.1.4 2.3.6 3.6.6.6 0 1 .4 1 1V20c0 .6-.4 1-1 1C10.6 21 3 13.4 3 4c0-.6.4-1 1-1h3.5c.6 0 1 .4 1 1 0 1.3.2 2.5.6 3.6.1.3 0 .7-.2 1z"/></svg>
          +1 555 284 6193
        </li>
        <li>
          <svg viewBox="0 0 24 24" aria-hidden="true"><path d="M2 5h20v14H2z M3.5 6.5 12 13l8.5-6.5" stroke="#434f42" stroke-width="1.5"/></svg>
          po@FundTarvel.example
        </li>
        <li>
          <svg viewBox="0 0 24 24" aria-hidden="true"><circle cx="12" cy="12" r="10"/><path d="M2 12h20M12 2c3 3 3 17 0 20M12 2c-3 3-3 17 0 20" stroke="#434f42" stroke-width="1.3" fill="none"/></svg>
          www.FundTarvel.example
        </li>
      </ul>
    </div>
  </section>
</div>
</body>
</html>
```